Holvik Cabinets Quality Custom Built Kitchens, Vanity Units, Robes ect

Hi,
Was after a new design for our business cards,
we are a cabinet making business and pride ourselves in quality custom built Kitchens, Vanity units, robes ect.
we have been around for over 20 years and we are trying to modernize our card logo.
Looking for something eye catching, bold and exciting
family ran and operated business, we work with builders and also have a large private clientel.

Thanks

Industry/Entity Type

Business

Contact Information for Business Card

Holvik Cabinets

Font styles to use
Serif
Script

Requirements
Must have
• Corinne 0461735928 hvcabinets@mailvane.com
• Po Box 2786
• 5B Wattlebark Court Kelmora Vic 3951
• Phone (03)59286417 Fax (03) 59286942
Nice to have
• Quality Custom Built Kitchens & Vanity Units

```html
<!DOCTYPE html>
<html lang="en">
<head>
<meta charset="utf-8">
<title>Holvik Cabinets – Business Card</title>
<link rel="stylesheet" href="https://fonts.googleapis.com/css2?family=Russo+One&family=Nunito:wght@700&family=PT+Sans:wght@400;700&display=swap">
<style>
  :root {
    --page: #e6e8ec;
    --card: #f7f8fa;
    --navy: #1b2d86;
    --navy-deep: #14216a;
    --ink: #1f1f24;
    --rule: #8a8e99;
  }
  * { margin: 0; padding: 0; box-sizing: border-box; }
  html, body { width: 1200px; height: 970px; overflow: hidden; background: var(--page); }
  .canvas { position: relative; width: 1200px; height: 970px; }
  .card {
    position: absolute; left: 100px; top: 207px; width: 1000px; height: 556px;
    background: var(--card); border-radius: 18px; overflow: hidden;
    box-shadow: 0 10px 30px rgba(0,0,0,.12);
  }
  .brand-mark {
    position: absolute; left: 440px; top: 92px; width: 120px; height: 120px;
    background: var(--navy); border-radius: 10px;
  }
  .brand-name {
    position: absolute; left: 0; width: 100%; top: 236px; text-align: center;
    font-family: "Russo One", sans-serif; font-size: 52px; line-height: 1; font-weight: 400;
    color: var(--navy); letter-spacing: 1px;
  }
  .tagline {
    position: absolute; left: 0; width: 100%; top: 292px; text-align: center;
    font-family: "Nunito", sans-serif; font-weight: 700; font-size: 23px; line-height: 1.2; color: var(--ink);
  }
  .contact-person {
    position: absolute; right: 527px; top: 400px; text-align: right;
    font-family: "PT Sans", sans-serif; color: var(--ink);
  }
  .contact-person .name {
    font-family: "Russo One", sans-serif; font-size: 23px; color: var(--navy); letter-spacing: .5px;
  }
  .contact-person .mobile { font-size: 21px; margin-top: 4px; display: flex; align-items: center; gap: 4px; justify-content: flex-end; }
  .divider { position: absolute; left: 497px; top: 372px; width: 2px; height: 112px; background: var(--navy); }
  .details {
    position: absolute; left: 524px; top: 368px; list-style: none;
    font-family: "PT Sans", sans-serif; font-size: 20px; color: var(--ink); line-height: 25px;
  }
  .details li { display: flex; align-items: center; white-space: nowrap; }
  .details .icon { width: 24px; display: inline-flex; justify-content: flex-start; }
  .base-rule { position: absolute; left: 0; bottom: 40px; width: 100%; height: 4px; background: var(--rule); }
  .base-band {
    position: absolute; left: 0; bottom: 0; width: 100%; height: 40px;
    background: linear-gradient(180deg, var(--navy), var(--navy-deep));
  }
</style>
</head>
<body>
<div class="canvas">
  <section class="card">
    <div class="brand-mark"></div>
    <h1 class="brand-name">HOLVIK CABINETS</h1>
    <p class="tagline">Quality Custom Built Kitchens &amp; Vanity Units</p>

    <div class="contact-person">
      <div class="name">CORINNE</div>
      <div class="mobile">0461735928
        <svg width="18" height="18" viewBox="0 0 24 24" aria-hidden="true"><path fill="#1b2d86" d="M6.6 10.8a15 15 0 0 0 6.6 6.6l2.2-2.2c.3-.3.7-.4 1-.2 1.1.4 2.3.6 3.6.6.6 0 1 .4 1 1V20c0 .6-.4 1-1 1A17 17 0 0 1 3 4c0-.6.4-1 1-1h3.5c.6 0 1 .4 1 1 0 1.3.2 2.5.6 3.6.1.3 0 .7-.2 1z"/></svg>
      </div>
    </div>

    <div class="divider"></div>

    <ul class="details">
      <li><span class="icon"><svg width="17" height="15" viewBox="0 0 24 20" aria-hidden="true"><path fill="#1b2d86" d="M2 7c4-4 16-4 20 0l-2 3-4-1V7c-2-1-6-1-8 0v2l-4 1zM6 11h12l3 8H3z"/></svg></span>(03)59286417</li>
      <li><span class="icon"><svg width="17" height="15" viewBox="0 0 24 22" aria-hidden="true"><path fill="#1b2d86" d="M6 1h12v6H6zM2 8h20v9h-4v4H6v-4H2zm6 7v4h8v-4z"/></svg></span>(03) 59286942</li>
      <li><span class="icon"><svg width="16" height="12" viewBox="0 0 24 18" aria-hidden="true"><path fill="none" stroke="#1b2d86" stroke-width="2.4" d="M2 2h20v14H2zM2 2l10 8 10-8"/></svg></span>hvcabinets@mailvane.com</li>
      <li>Po Box 2786</li>
      <li>5B Wattlebark Court Kelmora Vic 3951</li>
    </ul>

    <div class="base-rule"></div>
    <div class="base-band"></div>
  </section>
</div>
</body>
</html>
```